General Contractors need a new Crisp updated Card Design

We need a new business card design for our company of 25 years based in Toronto call Holvaster Building Inc. : Our goal is to be the leading commercial contractors in Toronto by providing exceptional value to our clients. We work very hard to deliver professional, quality, service in conjunction with consistent price competitiveness to all of our clients on every single project.

Target Market(s)

Design & Build Clients

Industry/Entity Type

Construction Company

Contact Information for Business Card

Address:
18 North Tamlin Glen Road, Unit 57, Marbrook Vale, ON, K7T 2R9
Office: 905-218-5937

Holvasters Logo
Employee Job Description
Employee Cell Phone #
Employee Email
www.holvaster-example.com

Colors

Designer to choose colors to be used in the design.

Requirements
Must have
• Quote Company Saying:
• "Professional. Quality. Service."
Nice to have
• New Crisp up to date look. simple & fresh ( Not to Busy)
Should not have
• NO BLUE PRINTS ON THE BUSINESS CARDS

```html
<!DOCTYPE html>
<html lang="en">
<head>
<meta charset="utf-8">
<title>Holvaster Building Inc. — Business Card</title>
<link rel="stylesheet" href="https://fonts.googleapis.com/css2?family=Cinzel:wght@600&family=Lato:wght@400;700&display=swap">
<style>
  :root {
    --page: #e6e8e7;
    --card: #ffffff;
    --brand-green: #0b6b5d;
    --brand-green-light: #2f8a7b;
    --sage: #b8cec6;
    --icon-grey: #9aa3a0;
    --text-dark: #0b6b5d;
  }
  * { box-sizing: border-box; margin: 0; padding: 0; }
  html, body { width: 1200px; height: 900px; overflow: hidden; }
  body {
    background: var(--page);
    font-family: "Lato", sans-serif;
    position: relative;
  }
  .card {
    position: absolute;
    left: 240px;
    width: 720px;
    height: 411px;
    overflow: hidden;
    box-shadow: 0 6px 18px rgba(0,0,0,0.18);
  }
  .card--front { top: 36px; background: var(--brand-green); }
  .card--back { top: 468px; background: var(--card); }

  /* Front side */
  .front-motif {
    position: absolute;
    inset: 0;
    background: linear-gradient(200deg, var(--brand-green-light) 0%, var(--brand-green) 55%, #0a5f53 100%);
  }
  .front-wordmark {
    position: absolute;
    top: 34px;
    right: 44px;
    font-family: "Cinzel", serif;
    font-weight: 600;
    font-size: 30px;
    letter-spacing: 1px;
    color: #ffffff;
    text-align: right;
    line-height: 1.1;
  }

  /* Back side */
  .brand {
    position: absolute;
    top: 60px;
    left: 56px;
    display: flex;
    align-items: center;
    gap: 16px;
  }
  .brand-square {
    width: 58px;
    height: 58px;
    background: var(--brand-green);
  }
  .brand-name {
    font-family: "Cinzel", serif;
    font-weight: 600;
    font-size: 30px;
    line-height: 1.05;
    letter-spacing: 1px;
    color: var(--brand-green);
  }
  .contact-person {
    position: absolute;
    left: 56px;
    top: 222px;
    color: var(--text-dark);
  }
  .person-name { font-weight: 700; font-size: 18px; letter-spacing: 0.5px; }
  .person-role { font-size: 15px; margin-bottom: 10px; }
  .contact-line {
    display: flex;
    align-items: center;
    gap: 8px;
    font-size: 15px;
    line-height: 22px;
  }
  .contact-icon { width: 14px; height: 14px; flex: none; }
  .company-address {
    position: absolute;
    right: 40px;
    top: 188px;
    text-align: right;
    color: var(--text-dark);
    font-size: 14px;
    line-height: 20px;
  }
  .company-web { font-weight: 700; font-size: 15px; }
  .tagline-band { position: absolute; left: 0; bottom: 0; width: 720px; height: 120px; }
  .tagline {
    position: absolute;
    left: 0;
    right: 0;
    bottom: 20px;
    text-align: center;
    font-family: "Cinzel", serif;
    font-weight: 600;
    font-size: 17px;
    letter-spacing: 7px;
    color: #ffffff;
    transform: rotate(-3.97deg);
  }
</style>
</head>
<body>

  <section class="card card--front">
    <div class="front-motif" role="img" aria-label="Large abstract geometric motif in green and white"></div>
    <div class="front-wordmark">Holvaster<br>Building Inc.</div>
  </section>

  <section class="card card--back">
    <div class="brand">
      <div class="brand-square"></div>
      <div class="brand-name">Holvaster<br>Building Inc.</div>
    </div>

    <div class="contact-person">
      <div class="person-name">MARCUS DELLAWAY</div>
      <div class="person-role">managing director</div>
      <div class="contact-line">
        <svg class="contact-icon" viewBox="0 0 14 14"><rect x="0.5" y="0.5" width="13" height="13" rx="3" fill="none" stroke="var(--icon-grey)"/><rect x="3" y="4.5" width="8" height="5.5" fill="none" stroke="var(--icon-grey)"/><path d="M3 4.5 L7 7.5 L11 4.5" fill="none" stroke="var(--icon-grey)"/></svg>
        <span>m.dellaway@holvaster-example.com</span>
      </div>
      <div class="contact-line">
        <svg class="contact-icon" viewBox="0 0 14 14"><rect x="0.5" y="0.5" width="13" height="13" rx="3" fill="none" stroke="var(--icon-grey)"/><rect x="4.5" y="2.5" width="5" height="9" rx="1" fill="none" stroke="var(--icon-grey)"/></svg>
        <span>5550 218 604</span>
      </div>
      <div class="contact-line">
        <svg class="contact-icon" viewBox="0 0 14 14"><rect x="0.5" y="0.5" width="13" height="13" rx="3" fill="none" stroke="var(--icon-grey)"/><path d="M3 6 Q7 2 11 6 L10 7.5 L8.5 6.5 L5.5 6.5 L4 7.5 Z M4 9 H10 V11 H4 Z" fill="var(--icon-grey)"/></svg>
        <span>905 218 5937</span>
      </div>
    </div>

    <div class="company-address">
      18 North Tamlin Glen Road, Unit 57<br>
      Marbrook Vale, ON, K7T 2R9<br>
      <span class="company-web">www.holvaster-example.com</span>
    </div>

    <svg class="tagline-band" viewBox="0 0 720 120" aria-hidden="true">
      <polygon points="0,71 720,21 720,29 0,79" fill="var(--sage)"/>
      <polygon points="0,79 720,29 720,120 0,120" fill="var(--brand-green)"/>
    </svg>
    <div class="tagline">PROFESSIONAL . QUALITY . SERVICE .</div>
  </section>

</body>
</html>
```